Varro's Electrical & Solar Corflute Signage Design

So my plan is to put this design onto a 600 by 400 corflute sign (this sign will be printed out and cable tied to a fence FYI). I would like to have the name and the icon stand out. I need Varro's Electrical & Solar to be big and clear and I would like to have my "S" icon faded behind "Varro's Electrical & Solar" in the background.

I want to have my Lic No. - Top left with my ABN directly underneath. (I Want two ticks infront of them like this)
✓ Lic No. 582164K
✓ ABN 41 276 519 683

I want to have written on it: ALL ASPECTS OF ELECTRICAL (please use cool fonts and nothing too plain)
I also want to have: YOUR LOCAL TRUSTED ELECTRICIAN but if it looks too dicky then just have "all aspects of electrical" and just "free quotes • fast service" somewhere.
Directly underneath (smaller but still clear): FREE QUOTES • FAST SERVICE

At the bottom, I need my phone number big and clear - 0438 617 905 I would like this on a banner meaning like a cool strip at the bottom. (Please make the strip/banner look cool and not boring. Maybe shade the colour or something)
I also want the Facebook & Instagram icons on there so people can look us up on facebook & Instagram (make them match the colour of my logo or you could try any other colour that works)
Thank you so much!!

Colors

Designer to choose colors to be used in the design.

Requirements
Should not have
• no different colours other then the colours on my logo and icon

```html
<!DOCTYPE html>
<html lang="en">
<head>
<meta charset="UTF-8">
<title>Varro's Electrical &amp; Solar – Corflute Sign</title>
<link href="https://fonts.googleapis.com/css2?family=Russo+One&family=Oswald:wght@500;700&display=swap" rel="stylesheet">
<style>
  :root{
    --page:#e9ece9;
    --black:#050705;
    --deep:#0b1a0b;
    --green:#39e61f;
    --green-dark:#1d8f0e;
    --silver:#e6ebe6;
    --white:#ffffff;
  }
  *{margin:0;padding:0;box-sizing:border-box}
  html,body{width:720px;height:1200px;overflow:hidden;background:var(--page)}
  .sign{
    position:absolute;left:10px;top:366px;width:700px;height:467px;
    background:var(--black);overflow:hidden;
    border:3px solid var(--green-dark);
  }
  .sign__storm{
    position:absolute;inset:0;
    background:
      radial-gradient(ellipse 40% 30% at 18% 12%, rgba(57,230,31,.35), transparent 70%),
      radial-gradient(ellipse 40% 30% at 85% 30%, rgba(57,230,31,.28), transparent 70%),
      radial-gradient(ellipse 50% 30% at 50% 40%, rgba(57,230,31,.18), transparent 70%),
      linear-gradient(180deg, var(--deep), var(--black) 70%);
  }
  .credentials{
    position:absolute;right:40px;top:16px;list-style:none;
    font-family:"Oswald",sans-serif;font-weight:700;font-size:14px;color:var(--white);
    line-height:18px;
  }
  .credentials li{display:flex;align-items:center;gap:6px}
  .credentials svg{width:13px;height:13px}
  .brand{
    position:absolute;left:0;right:0;top:62px;text-align:center;
    font-family:"Russo One",sans-serif;color:var(--silver);
  }
  .brand__name{font-size:88px;line-height:88px;letter-spacing:2px}
  .brand__trade{font-size:24px;letter-spacing:6px;margin-top:2px}
  .tagline{
    position:absolute;left:0;right:0;top:192px;text-align:center;
    font-family:"Russo One",sans-serif;font-size:40px;color:var(--green);
    letter-spacing:1px;
  }
  .services{
    position:absolute;left:0;right:0;top:252px;text-align:center;
    font-family:"Oswald",sans-serif;font-weight:500;font-size:28px;
    color:var(--white);letter-spacing:2px;
  }
  .contact-bar{
    position:absolute;left:0;right:0;top:308px;height:100px;
    background:linear-gradient(180deg, var(--black), var(--deep));
    display:flex;align-items:center;justify-content:center;gap:30px;
  }
  .contact-bar__phone{
    font-family:"Oswald",sans-serif;font-weight:700;font-size:64px;
    color:var(--white);letter-spacing:2px;
  }
  .socials{display:flex;gap:8px}
  .socials span{width:30px;height:30px;border-radius:6px;background:var(--green)}
  .sign__strip{
    position:absolute;left:0;right:0;bottom:0;height:50px;
    background:linear-gradient(180deg, var(--green), var(--green-dark));
  }
</style>
</head>
<body>
  <section class="sign">
    <div class="sign__storm" role="img" aria-label="Green lightning bolts crackling across a black background"></div>

    <ul class="credentials">
      <li><svg viewBox="0 0 16 16"><path d="M2 8.5l4 4 8-9" fill="none" stroke="#39e61f" stroke-width="3"/></svg>Lic No. 582164K</li>
      <li><svg viewBox="0 0 16 16"><path d="M2 8.5l4 4 8-9" fill="none" stroke="#39e61f" stroke-width="3"/></svg>ABN 41 276 519 683</li>
    </ul>

    <div class="brand">
      <div class="brand__name">VARRO'S</div>
      <div class="brand__trade">ELECTRICAL &amp; SOLAR</div>
    </div>

    <h1 class="tagline">ALL ASPECTS OF ELECTRICAL</h1>
    <p class="services">FREE QUOTES • FAST SERVICE</p>

    <div class="contact-bar">
      <span class="contact-bar__phone">0438 617 905</span>
      <div class="socials" aria-label="Social media">
        <span></span><span></span><span></span>
      </div>
    </div>

    <div class="sign__strip"></div>
  </section>
</body>
</html>
```